Letter design, envelope design, and more

Hello, we the Varlo Gmbh are looking for our shop. Letter C5. Design does not have to be like a business card, so it can have straight lines. Only the color is important. The logo is the text under VaRLo omit.It should not be playful but Profesionel

Font styles to use
Sans Serif

Colors
0555a3
3176b5
85abd2
85cae6
34a7d8
0792cd
cee9f5
cfdfed
000000

Requirements
Must have
• Color like business card, Please, with the text under VaRLo, Correct address Benkelstr. 4 Zip code 9512 Goldach, as well as Couvert Without addressing only design and logo with VaRlo
Nice to have
• more writing articles
Should not have
• Not too colored, Text under VaRLo, bright colors

```html
<!DOCTYPE html>
<html lang="de">
<head>
<meta charset="utf-8">
<title>Varlo Gmbh – Briefpapier und Couvert</title>
<link href="https://fonts.googleapis.com/css2?family=Open+Sans:wght@400;600;700&display=swap" rel="stylesheet">
<style>
  :root {
    --backdrop: #6c8e9c;
    --paper: #f7f7f8;
    --brand-blue: #0555a3;
    --mid-blue: #3176b5;
    --soft-blue: #85abd2;
    --text-grey: #55606e;
    --faint: #e6eef6;
  }
  * { margin: 0; padding: 0; box-sizing: border-box; }
  html, body { width: 1200px; height: 905px; overflow: hidden; }
  body {
    background: var(--backdrop);
    font-family: "Open Sans", Arial, sans-serif;
    position: relative;
  }
  .letterhead, .envelope {
    position: absolute;
    background: var(--paper);
    overflow: hidden;
    box-shadow: 0 4px 10px rgba(0,0,0,0.18);
  }
  .letterhead { left: 73px; top: 78px; width: 506px; height: 716px; }
  .envelope { left: 641px; top: 447px; width: 505px; height: 238px; }
  .sheet-art { position: absolute; inset: 0; width: 100%; height: 100%; }

  .brand { position: absolute; display: flex; align-items: center; gap: 8px; }
  .brand-square { background: var(--brand-blue); }
  .brand-name {
    color: var(--brand-blue);
    font-weight: 700;
    line-height: 1;
    letter-spacing: 0.5px;
  }
  .letterhead .brand { left: 52px; top: 82px; }
  .letterhead .brand-square { width: 30px; height: 30px; }
  .letterhead .brand-name { font-size: 34px; }

  .watermark {
    position: absolute;
    left: 0; right: 0; top: 295px;
    text-align: center;
    color: var(--faint);
    font-weight: 700;
    font-size: 120px;
    line-height: 1;
  }

  .letter-footer {
    position: absolute;
    left: 0; right: 0; top: 657px;
    text-align: center;
    font-size: 9.5px;
    letter-spacing: 1px;
    color: var(--text-grey);
  }

  .envelope .brand { left: 22px; top: 88px; }
  .envelope .brand-square { width: 22px; height: 22px; }
  .envelope .brand-name { font-size: 24px; }

  .contact-list {
    position: absolute;
    left: 30px; top: 144px;
    list-style: none;
    font-size: 9.5px;
    color: var(--text-grey);
  }
  .contact-list li { display: flex; align-items: center; gap: 9px; height: 15px; }
  .contact-list svg { width: 7px; height: 7px; fill: var(--brand-blue); flex: none; }
</style>
</head>
<body>

<section class="letterhead" aria-label="Briefpapier">
  <svg class="sheet-art" viewBox="0 0 506 716" preserveAspectRatio="none" aria-hidden="true">
    <rect width="506" height="160" fill="var(--brand-blue)"/>
    <path d="M180 22 C300 28 420 62 506 96 V160 H180 Z" fill="var(--soft-blue)"/>
    <path d="M0 38 C60 28 140 20 205 22 C320 28 430 82 506 130 V716 H0 Z" fill="var(--paper)"/>
    <path d="M0 605 C50 640 100 678 152 716 H0 Z" fill="var(--brand-blue)"/>
    <path d="M0 662 C28 680 55 698 80 716 H0 Z" fill="var(--soft-blue)"/>
  </svg>

  <div class="brand">
    <span class="brand-square"></span>
    <span class="brand-name">VaRLo Gmbh</span>
  </div>

  <div class="watermark" aria-hidden="true">VaRLo</div>

  <p class="letter-footer">0712 880 356 | office@varlo-shop.ch | UID: 52118604273</p>
</section>

<section class="envelope" aria-label="Couvert">
  <svg class="sheet-art" viewBox="0 0 505 238" preserveAspectRatio="none" aria-hidden="true">
    <rect width="505" height="140" fill="var(--brand-blue)"/>
    <path d="M180 20 C300 26 420 60 505 92 V140 H180 Z" fill="var(--soft-blue)"/>
    <path d="M0 34 C60 24 140 18 205 20 C320 26 430 82 505 128 V238 H0 Z" fill="var(--paper)"/>
  </svg>

  <div class="brand">
    <span class="brand-square"></span>
    <span class="brand-name">VaRlo Gmbh</span>
  </div>

  <ul class="contact-list">
    <li><svg viewBox="0 0 10 10"><rect x="0" y="2" width="10" height="6" rx="1"/></svg>hello@varlo-shop.ch</li>
    <li><svg viewBox="0 0 10 10"><path d="M2 0 L4 2 L3 4 C4 6 5 7 6 7 L8 6 L10 8 L8 10 C4 10 0 6 0 2 Z"/></svg>+41 71 555 02 18</li>
    <li><svg viewBox="0 0 10 10"><path d="M5 0 C2.5 0 1 2 1 4 C1 6.5 5 10 5 10 C5 10 9 6.5 9 4 C9 2 7.5 0 5 0 Z M5 2.5 A1.5 1.5 0 1 1 5 5.5 A1.5 1.5 0 1 1 5 2.5 Z"/></svg>Benkelstr. 4, 9512 Goldach</li>
    <li><svg viewBox="0 0 10 10"><circle cx="5" cy="5" r="5"/></svg>www.varlo-shop.ch</li>
  </ul>
</section>

</body>
</html>
```